Modern Design for Eyecare business - Vision Center, Optometry, Eye Doctors, Health Care

Create a sleek, modern, sharp homepage design for a eyecare center in Oklahoma City, OK. The vision center provides eyecare health services along with prescription eyewear.

I have included the logo which should be the basis of the designs look and feel. No other imagery was given so feel free to include stock photos and illustrations that you believe give the design a fresh look.

Please do not include stock photos of people/humans

I have included a document that provides some verbiage for the design as well as the designs main navigation.

They have an existing website http://www.bluepineoptics.example/ but are not happy with it. The new design should be different than their existing design.

List of websites for inspiration:
http://www.harborfaith.example
https://www.meadowlenspartners.example
http://www.brightsmiledental.example/
https://www.keltro.example

Target Market(s)

all ages

industry: Health, Eyewear, Eyecare, Optometry

Industry/Entity Type

Health

Number of Pages Required

1 page

Requirements
Must have
• Light color scheme that matches logo colors.
• Sophisticated, sleek design that resembles the logo's style.
Nice to have
• Large, full width visual banner with a 'contact us, etc' call-to-action between header and homepage content
Should not have
• No stock images of people/humans.
• Other forms of stock photos/illustrations are fine.

```html
<!DOCTYPE html>
<html lang="en">
<head>
<meta charset="utf-8">
<title>Bluepine Optics</title>
<link href="https://fonts.googleapis.com/css2?family=Open+Sans:wght@400;600;700&family=Raleway:wght@400;600;700&display=swap" rel="stylesheet">
<style>
:root{
  --blue:#3d7fca;
  --blue-dark:#2b5f9e;
  --navy:#2d4a6b;
  --navy-deep:#233a55;
  --ink:#333b45;
  --muted:#7a838d;
  --light:#f2f4f6;
  --line:#dde2e7;
  --footer:#2f3338;
  --footer-deep:#24272b;
  --white:#fff;
}
*{box-sizing:border-box;margin:0;padding:0}
html,body{width:1200px;height:2688px;overflow:hidden}
body{font-family:"Open Sans",sans-serif;color:var(--ink);background:var(--white);position:relative;font-size:13px;line-height:1.6}
h1,h2,h3,h4{font-family:"Raleway",sans-serif;font-weight:600}
.topbar{height:32px;background:var(--blue);color:var(--white);font-size:12px;display:flex;justify-content:flex-end;align-items:center;gap:30px;padding-right:150px}
.topbar span{display:flex;align-items:center;gap:6px}
.header{height:80px;display:flex;align-items:center;justify-content:space-between;padding:0 150px}
.brand{display:flex;align-items:center;gap:10px;font-family:"Raleway",sans-serif;font-size:24px;font-weight:600;color:var(--blue-dark)}
.brand i{width:14px;height:14px;border-radius:50%;background:var(--blue);display:block}
.nav{display:flex;gap:24px;font-size:12.5px;color:var(--ink)}
.nav a:first-child{color:var(--blue)}
.hero{position:relative;height:360px;background:linear-gradient(110deg,#e9eef3 0%,#c7d1da 45%,#8e9aa6 100%)}
.hero .photo{position:absolute;inset:0}
.hero .arrow{position:absolute;top:150px;width:40px;height:56px;background:var(--navy);display:flex;align-items:center;justify-content:center}
.consult{position:absolute;right:150px;top:10px;width:290px;height:390px;background:var(--white);box-shadow:0 4px 18px rgba(0,0,0,.15);z-index:2}
.consult header{background:var(--blue);color:var(--white);text-align:center;padding:18px 0 14px}
.consult header small{display:block;font-size:12px}
.consult header strong{font-family:"Raleway",sans-serif;font-size:20px;letter-spacing:.5px}
.consult form{padding:16px 22px}
.field{height:34px;border:1px solid var(--line);margin-bottom:10px;padding:0 10px;font-size:11px;color:var(--muted);display:flex;align-items:center}
.field.tall{height:70px;align-items:flex-start;padding-top:8px}
.btn{display:inline-block;border:1px solid var(--blue);color:var(--blue);font-size:12px;padding:6px 20px;border-radius:3px}
.btn.light{border-color:var(--white);color:var(--white)}
.consult .btn{display:block;width:110px;margin:8px auto 0;text-align:center}
.welcome{padding:34px 150px 0;width:800px}
.welcome h2{font-size:22px;color:var(--ink);margin-bottom:10px}
.welcome p{color:var(--muted);font-size:12.5px;margin-bottom:14px;width:620px}
.features{display:flex;gap:0;margin:40px 150px 0;height:300px}
.feature{flex:1;color:var(--white);padding:26px 24px;position:relative}
.feature:nth-child(1){background:var(--blue)}
.feature:nth-child(2){background:#4a8ad2}
.feature:nth-child(3){background:var(--blue-dark)}
.feature h3{font-size:21px;line-height:1.25;margin-bottom:14px}
.feature p{font-size:12px;opacity:.9;margin-bottom:10px}
.feature ul{list-style:none;font-size:12px}
.feature li::before{content:"›";margin-right:8px}
.feature .btn{position:absolute;left:24px;bottom:24px}
.appointment{margin-top:30px;height:400px;background:linear-gradient(180deg,var(--navy) 0%,var(--navy-deep) 100%);color:var(--white);text-align:center;padding-top:40px}
.section-title{font-family:"Raleway",sans-serif;font-size:22px;font-weight:600}
.mark{width:22px;height:4px;background:var(--blue);margin:10px auto 26px}
.appointment .mark{background:var(--white)}
.appt-grid{width:900px;margin:0 auto;display:grid;grid-template-columns:repeat(3,1fr);gap:14px}
.appt-grid .field{border-color:rgba(255,255,255,.35);color:rgba(255,255,255,.7);background:rgba(255,255,255,.05)}
.appt-grid .wide{grid-column:1/4;height:60px;align-items:flex-start;padding-top:8px}
.appointment .btn{margin-top:22px}
.doctors{padding-top:40px;text-align:center}
.doc-row{position:relative;height:420px;margin-top:0}
.doc-band{position:absolute;left:0;right:0;top:60px;height:300px;background:var(--light)}
.doc-photo{position:absolute;left:280px;top:0;width:300px;height:420px;background:linear-gradient(180deg,#dfe6ec 0%,#c3cfd9 100%)}
.doc-info{position:absolute;left:640px;top:100px;width:420px;text-align:left}
.doc-info h3{font-size:22px;color:var(--ink);margin-bottom:10px}
.doc-info p{font-size:12px;color:var(--muted);margin-bottom:10px}
.pager{position:absolute;left:0;top:320px;display:flex}
.pager span{width:40px;height:40px;background:var(--footer);display:flex;align-items:center;justify-content:center}
.reviews{padding-top:30px;text-align:center}
.quote-box{position:relative;width:760px;margin:0 auto;border:1px solid var(--line);padding:26px 60px 22px;font-size:12px;color:var(--muted)}
.quote-box .q{font-size:46px;line-height:1;color:#c8cfd6;font-family:Georgia,serif}
.review-side{position:absolute;top:50%;width:22px;height:22px;border-radius:50%;border:1px solid var(--line);margin-top:-11px}
.avatars{display:flex;justify-content:center;gap:30px;margin-top:-10px}
.avatars span{width:46px;height:46px;border-radius:50%;background:#cfd6dd;border:3px solid var(--white)}
.avatars span.on{width:56px;height:56px;background:#b9c3cc}
.reviewer{font-size:12px;margin-top:6px}
.reviewer b{display:block;color:var(--ink)}
.footer{position:absolute;left:0;right:0;top:2390px;height:298px;background:var(--footer);color:#c9cdd2}
.footer .cols{display:flex;gap:40px;padding:40px 150px 0}
.footer .col{flex:1}
.footer h4{color:var(--white);font-size:14px;margin-bottom:12px}
.footer ul{list-style:none;font-size:11.5px;line-height:1.9}
.footer li::before{content:"› ";color:var(--blue)}
.footer .contact li::before{content:""}
.copyright{position:absolute;left:0;right:0;bottom:0;height:36px;background:var(--footer-deep);font-size:11px;text-align:center;line-height:36px;color:#8d949b}
</style>
</head>
<body>
<div class="topbar">
  <span><svg width="12" height="12" viewBox="0 0 24 24"><path fill="#fff" d="M6.6 10.8a15 15 0 006.6 6.6l2.2-2.2a1 1 0 011-.25 11.4 11.4 0 003.6.6 1 1 0 011 1V20a1 1 0 01-1 1A17 17 0 013 4a1 1 0 011-1h3.5a1 1 0 011 1 11.4 11.4 0 00.6 3.6 1 1 0 01-.25 1z"/></svg>405-555-0142</span>
  <span><svg width="12" height="12" viewBox="0 0 24 24"><path fill="#fff" d="M12 2a7 7 0 00-7 7c0 5 7 13 7 13s7-8 7-13a7 7 0 00-7-7zm0 9.5A2.5 2.5 0 1112 6a2.5 2.5 0 010 5.5z"/></svg>405-555-0143</span>
</div>
<header class="header">
  <div class="brand"><i></i>Bluepine Optics</div>
  <nav class="nav"><a>Home</a><a>About Services</a><a>Doctors</a><a>Patient Info</a><a>Product Reviews</a><a>Schedule Appointment</a><a>Contact</a></nav>
</header>
<section class="hero">
  <div class="photo" role="img" aria-label="Close-up of an optometrist trial frame with lenses during an eye exam"></div>
  <div class="arrow" style="left:0"><svg width="12" height="18" viewBox="0 0 12 18"><path d="M10 2L3 9l7 7" stroke="#fff" stroke-width="2" fill="none"/></svg></div>
  <div class="arrow" style="right:0"><svg width="12" height="18" viewBox="0 0 12 18"><path d="M2 2l7 7-7 7" stroke="#fff" stroke-width="2" fill="none"/></svg></div>
  <aside class="consult">
    <header><small>Contact Us Today for</small><strong>FREE CONSULTATION</strong></header>
    <form>
      <div class="field">Name</div>
      <div class="field">Email</div>
      <div class="field">Phone</div>
      <div class="field tall">Message</div>
      <span class="btn">Submit ›</span>
    </form>
  </aside>
</section>
<section class="welcome">
  <h2>Welcome to Bluepine Optics</h2>
  <p>We are proud to offer complete eye care for every member of your family. Our doctors use modern tools to check your vision, find eye disease early, and fit you with the right glasses or contacts. We take time to listen, answer your questions and help you see clearly every day.</p>
  <span class="btn">Read More ›</span>
</section>
<section class="features">
  <article class="feature">
    <h3>Check Our Special Services</h3>
    <ul><li>Comprehensive Exams</li><li>Contact Lenses</li><li>Eye Glasses</li><li>Children's Vision</li><li>Laser Surgery Care</li><li>Dry Eye Relief</li></ul>
    <span class="btn light">View All ›</span>
  </article>
  <article class="feature">
    <h3>True Experts of Eye Care</h3>
    <p>Our optometrists have years of training in primary eye care. From routine exams to managing glaucoma and diabetes, we bring skill and care to every visit.</p>
    <span class="btn light">Read More ›</span>
  </article>
  <article class="feature">
    <h3>Problems and Diseases</h3>
    <p>Learn about common eye conditions and how we treat them.</p>
    <ul><li>Cataracts</li><li>Glaucoma</li><li>Macular Degeneration</li><li>Diabetic Eye</li></ul>
    <span class="btn light">View All ›</span>
  </article>
</section>
<section class="appointment">
  <h2 class="section-title">Appointment Request</h2>
  <div class="mark"></div>
  <form class="appt-grid">
    <div class="field">First Name</div><div class="field">Last Name</div><div class="field">Email</div>
    <div class="field">Phone</div><div class="field">Preferred Date</div><div class="field">Preferred Time</div>
    <div class="field wide">Comments</div>
  </form>
  <span class="btn light">Submit ›</span>
</section>
<section class="doctors">
  <h2 class="section-title">Meet our Doctors</h2>
  <div class="mark"></div>
  <div class="doc-row">
    <div class="doc-band"></div>
    <div class="doc-photo" role="img" aria-label="Portrait photo of the eye doctor in a white coat"></div>
    <div class="doc-info">
      <h3>Dr. Owen Hale</h3>
      <p>Dr. Hale has cared for patients in Oklahoma City for over fifteen years. He earned his doctor of optometry degree with honors and is known for his calm, friendly approach.</p>
      <p>He enjoys helping children and adults alike, and takes pride in finding the best lenses for each lifestyle.</p>
      <span class="btn">Read More ›</span>
    </div>
    <div class="pager">
      <span><svg width="10" height="14" viewBox="0 0 10 14"><path d="M8 1L2 7l6 6" stroke="#fff" stroke-width="2" fill="none"/></svg></span>
      <span style="background:#454a50"><svg width="10" height="14" viewBox="0 0 10 14"><path d="M2 1l6 6-6 6" stroke="#fff" stroke-width="2" fill="none"/></svg></span>
    </div>
  </div>
</section>
<section class="reviews">
  <h2 class="section-title">Patient Reviews</h2>
  <div class="mark"></div>
  <div class="quote-box">
    <span class="review-side" style="left:-11px"></span>
    <span class="review-side" style="right:-11px"></span>
    <div class="q">&ldquo;</div>
    <p>Dr. Hale is so kind and patient. The staff is friendly and the office runs on time. I would recommend this clinic to anyone who needs eye care.</p>
  </div>
  <div class="avatars" style="margin-top:14px"><span></span><span class="on"></span><span></span></div>
  <div class="reviewer"><b>Marcus Reed</b>Happy Patient</div>
</section>
<footer class="footer">
  <div class="cols">
    <div class="col"><h4>Quick Links</h4><ul><li>About Services</li><li>Vision Benefits</li><li>Patient Info</li><li>Product Reviews</li><li>Schedule Appointment</li><li>Contact</li></ul></div>
    <div class="col"><h4>Our Services</h4><ul><li>General</li><li>Eye Examinations</li><li>Contact Lenses</li><li>Eye Care for Kids</li><li>Laser Surgery</li><li>Dry Eye Treatment</li></ul></div>
    <div class="col"><h4>Problems &amp; Diseases</h4><ul><li>Eye Diseases</li><li>Vision Problems</li><li>Glaucoma</li></ul></div>
    <div class="col"><h4>Contact Us</h4><ul class="contact"><li>2140 Ridgeview Ave</li><li>Oklahoma City, OK 73100</li><li>405-555-0142</li><li>405-555-0143</li><li>hello@bluepineoptics.example</li></ul></div>
  </div>
  <div class="copyright">Copyright &copy; 2016 All Rights Reserved Bluepine Optics</div>
</footer>
</body>
</html>
```